Quorenta - Automated robotic Inspection with AI need new business cards

We need a new design of our business cards. The company is focused on automated quality control at high speed with unmatched results. We have a logo but need a more forward leaning business card that shows that we are delivering cutting edge technology.

Contact Information for Business Card

Name
Position
Adress
Phone
Email
e.g.
Lotta Berglund
Chief Financial Officer (CFO)

Quorenta Sweden AB
Rönnvägen 14, SE-175 43 JÄRFÄLLA, Sweden
Mobile: +46701 23 45 67 | Office: +46 8 52 61 74
www.quorenta-example.com

Font styles to use
Sans Serif

```html
<!DOCTYPE html>
<html lang="en">
<head>
<meta charset="utf-8">
<title>Quorenta Business Card</title>
<link rel="stylesheet" href="https://fonts.googleapis.com/css2?family=Open+Sans:wght@400;600;700&family=Michroma&display=swap">
<style>
  :root {
    --bg: #2a2a2a;
    --brand-blue: #1e5a8a;
    --brand-blue-light: #23679c;
    --brand-blue-deep: #1a5282;
    --paper: #ffffff;
    --text-grey: #8c8c8c;
    --shadow: rgba(0, 0, 0, 0.45);
  }
  * { box-sizing: border-box; margin: 0; padding: 0; }
  html, body {
    width: 1200px; height: 900px; overflow: hidden;
    background: var(--bg);
    font-family: "Open Sans", Arial, sans-serif;
  }
  .card {
    position: absolute; left: 280px;
    width: 640px; height: 366px;
    box-shadow: 0 12px 30px var(--shadow);
    overflow: hidden;
  }
  .card--back { top: 60px; background: var(--brand-blue); }
  .card--front { top: 474px; background: var(--paper); }

  .back-pattern {
    position: absolute; inset: 0;
    background: radial-gradient(ellipse at 60% 40%, var(--brand-blue-light) 0%, var(--brand-blue) 55%, var(--brand-blue-deep) 100%);
  }
  .back-name {
    position: absolute; left: 40px; bottom: 36px;
    color: var(--paper); font-weight: 700; font-size: 20px;
  }

  .brand {
    position: absolute; left: 36px; top: 26px;
    display: flex; align-items: center; gap: 10px;
  }
  .brand-dot {
    width: 22px; height: 22px; border-radius: 50%;
    background: var(--brand-blue);
  }
  .brand-name {
    color: var(--brand-blue); font-weight: 700; font-size: 40px; letter-spacing: 1px;
  }
  .person { position: absolute; left: 36px; top: 122px; }
  .person-name {
    font-family: "Michroma", "Open Sans", sans-serif;
    color: var(--brand-blue); font-size: 22px; letter-spacing: 1px;
    white-space: nowrap;
  }
  .person-title { color: var(--text-grey); font-size: 17px; margin-top: 2px; }

  .phones { position: absolute; left: 36px; top: 196px; }
  .phone-row {
    display: flex; align-items: center; gap: 10px;
    color: var(--text-grey); font-size: 18px; line-height: 26px;
  }
  .phone-row svg { width: 16px; height: 18px; fill: var(--brand-blue); }

  .address {
    position: absolute; left: 36px; top: 270px;
    color: var(--text-grey); font-size: 17px; line-height: 23px;
    white-space: nowrap;
  }

  .corner-motif {
    position: absolute; left: 350px; top: 150px;
    width: 290px; height: 216px;
  }
  .web-links {
    position: absolute; right: 20px; bottom: 22px;
    color: var(--paper); font-size: 16px; line-height: 28px; text-align: right;
  }
  .web-row {
    display: flex; align-items: center; justify-content: flex-end; gap: 10px;
    white-space: nowrap;
  }
  .web-row svg { width: 18px; height: 18px; flex: none; }
</style>
</head>
<body>

<section class="card card--back">
  <div class="back-pattern" role="img" aria-label="Repeating embossed brand pattern in blue"></div>
  <span class="back-name">Quorenta</span>
</section>

<section class="card card--front">
  <div class="brand">
    <span class="brand-dot"></span>
    <span class="brand-name">Quorenta</span>
  </div>

  <div class="person">
    <div class="person-name">LOTTA&nbsp; BERGLUND</div>
    <div class="person-title">Chief Financial Officer (CFO)</div>
  </div>

  <div class="phones">
    <div class="phone-row">
      <svg viewBox="0 0 24 24" aria-hidden="true"><path d="M6.6 10.8a15.1 15.1 0 0 0 6.6 6.6l2.2-2.2a1 1 0 0 1 1-.25 11.4 11.4 0 0 0 3.6.57 1 1 0 0 1 1 1V20a1 1 0 0 1-1 1A17 17 0 0 1 3 4a1 1 0 0 1 1-1h3.5a1 1 0 0 1 1 1c0 1.25.2 2.45.57 3.57a1 1 0 0 1-.25 1z"/></svg>
      <span>+46 8 52 61 74</span>
    </div>
    <div class="phone-row">
      <svg viewBox="0 0 24 24" aria-hidden="true"><path d="M7 1h10a2 2 0 0 1 2 2v18a2 2 0 0 1-2 2H7a2 2 0 0 1-2-2V3a2 2 0 0 1 2-2zm0 3v14h10V4zm5 15.5a1 1 0 1 0 0 2 1 1 0 0 0 0-2z"/></svg>
      <span>+46701 23 45 67</span>
    </div>
  </div>

  <div class="address">
    Quorenta Sweden AB<br>
    Rönnvägen 14, SE-175 43 JÄRFÄLLA<br>
    Sweden
  </div>

  <svg class="corner-motif" viewBox="0 0 290 216" preserveAspectRatio="none" role="img" aria-label="Large brand motif in blue filling the lower right corner">
    <path d="M0 216 C 10 120, 110 30, 290 0 L 290 216 Z" fill="var(--brand-blue)"/>
  </svg>

  <div class="web-links">
    <div class="web-row">
      <span>info@quorenta-example.com</span>
      <svg viewBox="0 0 24 24" aria-hidden="true"><rect x="2" y="5" width="20" height="14" fill="#fff"/><path d="M2 5l10 8 10-8" fill="none" stroke="#1e5a8a" stroke-width="1.8"/></svg>
    </div>
    <div class="web-row">
      <span>www.quorenta-example.com</span>
      <svg viewBox="0 0 24 24" aria-hidden="true"><circle cx="12" cy="12" r="9.5" fill="none" stroke="#fff" stroke-width="2"/><ellipse cx="12" cy="12" rx="4" ry="9.5" fill="none" stroke="#fff" stroke-width="1.6"/><path d="M3 9h18M3 15h18" stroke="#fff" stroke-width="1.6"/></svg>
    </div>
  </div>
</section>

</body>
</html>
```